r-plumavector needs new website

need to get completely new updated site for r-plumavector.com
general business concepts can be started from that site and I can offer specifick input about business operations and goals. would like to offer on-line ordering, service requests, and payments if possible.

```html
<!DOCTYPE html>
<html lang="en">
<head>
<meta charset="utf-8">
<title>r-plumavector — Lockbox &amp; Remittance Processing</title>
<link href="https://fonts.googleapis.com/css2?family=Montserrat:wght@400;600;700;800&family=Open+Sans:wght@400;600;700&display=swap" rel="stylesheet">
<style>
:root{
  --red:#e3101f;
  --red-dark:#b30a16;
  --red-deep:#c90c19;
  --ink:#1b1b1b;
  --text:#555;
  --muted:#888;
  --light:#f2f2f2;
  --line:#dcdcdc;
  --white:#fff;
  --dark:#161616;
}
*{box-sizing:border-box;margin:0;padding:0}
html,body{width:1200px;height:4032px;overflow:hidden}
body{font-family:'Open Sans',Arial,sans-serif;color:var(--text);background:var(--white);position:relative}
section,header,footer{position:absolute;left:0;width:1200px}

/* header */
.site-header{top:0;height:110px;z-index:3}
.header-top{height:64px;background:rgba(255,255,255,.94);display:flex;align-items:center;justify-content:space-between;padding:0 60px}
.logo{display:flex;align-items:center;gap:10px;font-family:'Montserrat',sans-serif;font-weight:800;font-size:26px;color:var(--ink)}
.logo-dot{width:20px;height:20px;border-radius:50%;background:var(--red)}
.header-contact{display:flex;gap:28px;font-size:13px;color:var(--ink)}
.header-contact span{display:flex;align-items:center;gap:7px}
.main-nav{position:absolute;right:300px;top:64px;display:flex;background:var(--red)}
.main-nav a{display:block;padding:11px 24px;color:#fff;text-decoration:none;font-family:'Montserrat',sans-serif;font-size:14px;font-weight:600;border-right:1px solid rgba(255,255,255,.3)}
.main-nav a.active{background:var(--red-dark)}

/* hero */
.hero{top:0;height:520px;overflow:hidden}
.hero-photo{position:absolute;inset:0;background:
  radial-gradient(ellipse 340px 260px at 22% 40%,#d9cfc6 0%,rgba(217,207,198,0) 70%),
  radial-gradient(ellipse 420px 300px at 78% 75%,#cfd2d4 0%,rgba(207,210,212,0) 70%),
  linear-gradient(100deg,#6f6a66 0%,#a9a29b 30%,#8e8c8a 55%,#5d6a58 85%,#3f4a3d 100%)}
.hero-shade{position:absolute;inset:0;background:linear-gradient(180deg,rgba(0,0,0,.05) 0%,rgba(0,0,0,.38) 45%,rgba(0,0,0,.18) 100%)}
.hero-caption{position:absolute;left:152px;top:232px;width:896px;text-align:center}
.hero-lead{color:#fff;font-size:18px;margin-bottom:12px;text-shadow:0 1px 3px rgba(0,0,0,.6)}
.hero-title{border:3px solid var(--red);background:rgba(0,0,0,.12);padding:18px 10px;color:#fff;font-family:'Montserrat',sans-serif;font-weight:800;font-size:44px;letter-spacing:5px;line-height:1.25;text-shadow:0 2px 4px rgba(0,0,0,.45)}
.slide-arrow{position:absolute;width:30px;height:30px;border-radius:50%;background:var(--red);display:flex;align-items:center;justify-content:center}
.hero .slide-arrow{top:355px}
.slide-arrow.prev{left:50px}.slide-arrow.next{right:50px}

/* section titles */
.section-title{text-align:center;font-family:'Montserrat',sans-serif;font-weight:800;font-size:40px;letter-spacing:4px;color:var(--ink)}
.section-title em{font-style:normal;color:var(--red)}
.title-rule{width:70px;height:3px;background:var(--red);margin:10px auto 0}
.btn-dark{display:inline-block;background:var(--ink);color:#fff;font-size:12px;padding:9px 18px;text-decoration:none}

/* about */
.about{top:520px;height:640px;text-align:center;padding:30px 150px 0}
.about h3{font-family:'Montserrat',sans-serif;font-size:19px;color:var(--ink);margin:28px 0 16px}
.about p{font-size:13px;line-height:1.75;margin-bottom:16px}

/* mission */
.mission{top:1160px;height:640px;background:var(--light);overflow:hidden}
.mission-photo{position:absolute;right:0;top:0;width:760px;height:640px;background:
  radial-gradient(ellipse 200px 260px at 52% 60%,#8f9aa5 0%,rgba(143,154,165,0) 70%),
  radial-gradient(ellipse 180px 240px at 82% 62%,#6b7480 0%,rgba(107,116,128,0) 70%),
  linear-gradient(90deg,var(--light) 0%,#d6dadd 30%,#c0c5ca 100%)}
.mission-accent{position:absolute;left:0;top:0}
.mission-body{position:absolute;left:140px;top:72px;width:430px}
.mission-body .section-title{text-align:left}
.mission-body .title-rule{margin:10px 0 0}
.mission-body h3{font-family:'Montserrat',sans-serif;font-size:17px;color:var(--ink);margin:34px 0 12px}
.mission-body p{font-size:12.5px;line-height:1.7;margin-bottom:12px}

/* applications */
.applications{top:1800px;height:720px;background:var(--red);overflow:hidden}
.applications .section-title{color:#fff;margin-top:46px;position:relative}
.applications .title-rule{background:#fff;position:relative}
.app-grid{position:absolute;left:152px;top:140px;display:grid;grid-template-columns:repeat(4,215px);gap:14px 12px}
.app-item{height:235px;position:relative;background:
  radial-gradient(ellipse 80px 55px at 50% 56%,#8d9096 0%,#4b4e54 45%,rgba(40,40,44,0) 100%),
  linear-gradient(160deg,#3a3b3f 0%,#1a1a1c 60%,#0b0b0c 100%)}
.app-item:nth-child(3){background:radial-gradient(ellipse 90px 50px at 50% 58%,#6a6c70 0%,#2e2f32 55%,rgba(20,20,22,0) 100%),linear-gradient(160deg,#2c2c2e,#0c0c0d)}
.app-item:nth-child(4),.app-item:nth-child(8){background:radial-gradient(ellipse 85px 60px at 50% 55%,#f0f0f0 0%,#9aa0a8 35%,rgba(30,50,90,0) 100%),linear-gradient(160deg,#1f3766 0%,#0d1a33 100%)}
.app-item:nth-child(5),.app-item:nth-child(6){background:radial-gradient(ellipse 80px 60px at 50% 55%,#b3b7bd 0%,#3d5276 45%,rgba(15,30,60,0) 100%),linear-gradient(160deg,#1d3566 0%,#0a1530 100%)}
.app-item.featured{background:linear-gradient(rgba(170,8,20,.88),rgba(150,6,16,.92)),linear-gradient(160deg,#3a3b3f,#0b0b0c);display:flex;flex-direction:column;align-items:center;justify-content:center;color:#fff;font-size:15px;gap:6px;text-align:center;line-height:1.35}
.app-item.featured b{font-size:26px;font-weight:400}
.app-item .tag{width:20px;height:20px;background:var(--red);margin-top:8px}
.view-all{position:absolute;left:552px;top:648px;background:#111;color:#fff;font-size:12px;padding:8px 16px}

/* testimonials */
.testimonials{top:2520px;height:520px;background:var(--light)}
.testimonials .section-title{margin-top:90px}
.review-cards{position:absolute;left:140px;top:180px;display:flex;gap:130px}
.review-card{width:240px;height:280px;background:#fff;text-align:center;padding:24px 18px}
.avatar{width:64px;height:64px;border-radius:50%;background:linear-gradient(135deg,#d7c4ae,#6d5a4b);margin:0 auto 12px}
.review-card h4{font-family:'Montserrat',sans-serif;font-size:15px;color:var(--ink)}
.review-card small{font-size:11px;color:var(--muted)}
.review-card p{font-size:12px;line-height:1.6;margin-top:16px}
.testimonials .slide-arrow{top:305px}
.testimonials .slide-arrow.prev{background:#cfcfcf}

/* inquiry & contact */
.contact-area{top:3040px;height:560px}
.block-title{font-family:'Montserrat',sans-serif;font-weight:800;font-size:20px;letter-spacing:2px;color:var(--ink)}
.block-title em{font-style:normal;color:var(--red)}
.rule{width:60px;height:3px;background:var(--red);margin:8px 0 24px}
.inquiry{position:absolute;left:140px;top:50px;width:500px}
.inquiry-form{border:1px solid var(--line);padding:24px;display:grid;grid-template-columns:1fr 1fr;gap:14px}
.field{border:1px solid var(--line);height:36px;padding:0 12px;font-size:12px;color:var(--muted);display:flex;align-items:center}
.field.full{grid-column:1/3}
.field.message{height:100px;align-items:flex-start;padding-top:10px}
.submit{grid-column:1/3;justify-self:start;background:var(--ink);color:#fff;font-size:12px;padding:9px 18px}
.contact-details{position:absolute;left:780px;top:50px;width:290px;font-size:12px;line-height:1.6}
.contact-details p{margin-bottom:12px}
.contact-row{display:flex;gap:12px;margin-bottom:14px}
.contact-row strong{display:block;color:var(--ink);font-size:13px}

/* map */
.map{top:3600px;height:292px;background:
  radial-gradient(ellipse 180px 120px at 48% 55%,#cfe0c4 0%,rgba(207,224,196,0) 70%),
  radial-gradient(ellipse 220px 140px at 85% 30%,#dcd6ea 0%,rgba(220,214,234,0) 70%),
  radial-gradient(ellipse 200px 130px at 15% 70%,#f0e6cf 0%,rgba(240,230,207,0) 70%),
  linear-gradient(135deg,#ecebe6,#e2e3de 50%,#ebe8e1)}

/* footer */
.footer-nav{top:3892px;height:68px;background:var(--red);display:flex;align-items:center;justify-content:center}
.footer-nav nav{display:flex;gap:40px}
.footer-nav a{color:#fff;text-decoration:none;font-family:'Montserrat',sans-serif;font-size:14px;font-weight:600}
.social{position:absolute;right:60px;top:21px;display:flex;gap:8px}
.social span{width:26px;height:26px;border-radius:50%;border:2px solid #fff}
.copyright{top:3960px;height:72px;background:var(--dark);color:#aaa;font-size:12px;display:flex;align-items:center;padding-left:60px}
</style>
</head>
<body>

<section class="hero">
  <div class="hero-photo" role="img" aria-label="Photo of an office worker using a document scanner"></div>
  <div class="hero-shade"></div>
  <div class="hero-caption">
    <p class="hero-lead">r-plumavector offers the most cost effective multi-format capture system for</p>
    <h1 class="hero-title">LOCKBOX &amp; REMITTANCE<br>PROCESSING</h1>
  </div>
  <span class="slide-arrow prev"><svg width="12" height="12" viewBox="0 0 12 12"><path d="M8 1 3 6l5 5" stroke="#fff" stroke-width="2" fill="none"/></svg></span>
  <span class="slide-arrow next"><svg width="12" height="12" viewBox="0 0 12 12"><path d="m4 1 5 5-5 5" stroke="#fff" stroke-width="2" fill="none"/></svg></span>
</section>

<header class="site-header">
  <div class="header-top">
    <div class="logo"><span class="logo-dot"></span>r-plumavector</div>
    <div class="header-contact">
      <span><svg width="14" height="14" viewBox="0 0 24 24"><path fill="#e3101f" d="M6.6 10.8a15 15 0 0 0 6.6 6.6l2.2-2.2c.3-.3.7-.4 1-.2 1.1.4 2.3.6 3.6.6.6 0 1 .4 1 1V20c0 .6-.4 1-1 1A17 17 0 0 1 3 4c0-.6.4-1 1-1h3.5c.6 0 1 .4 1 1 0 1.3.2 2.5.6 3.6.1.3 0 .7-.2 1z"/></svg>555-014-2270</span>
      <span><svg width="14" height="14" viewBox="0 0 24 24"><path fill="#e3101f" d="M2 5h20v14H2zm2 2v.5l8 5 8-5V7z"/></svg>freeinfo@r-plumavector.com</span>
    </div>
  </div>
  <nav class="main-nav">
    <a class="active" href="#">Home</a><a href="#">About Us</a><a href="#">Our Mission</a><a href="#">Applications</a><a href="#">Contact Us</a>
  </nav>
</header>

<section class="about">
  <h2 class="section-title"><em>ABOUT</em> US</h2>
  <div class="title-rule"></div>
  <h3>We Provide Valuable Solutions</h3>
  <p>r-plumavector is an imaging solutions company based out of central Illinois. Being from a small town, we keep our roots in honesty and hospitality, yet our product solutions are on the cutting edge of technology.</p>
  <p>We not only provide our customers valuable solutions; we do it with the understanding that the needs of the institutions we serve are the reason to stay up to date on the latest advancements in the industry. From simple check scanners to complete corporate payment processing systems and everything in between, we have complete solutions that are cost effective and user friendly.</p>
  <a class="btn-dark" href="#">Read More &gt;&gt;</a>
</section>

<section class="mission">
  <div class="mission-photo" role="img" aria-label="Photo of two colleagues meeting in an office"></div>
  <svg class="mission-accent" width="1200" height="640" viewBox="0 0 1200 640"><polygon points="0,0 90,0 0,90" fill="#e3101f"/><polygon points="1200,550 1200,640 1110,640" fill="#e3101f"/></svg>
  <div class="mission-body">
    <h2 class="section-title"><em>OUR</em> MISSION</h2>
    <div class="title-rule"></div>
    <h3>How We Do Business</h3>
    <p>r-plumavector strives to be the leading provider of cost-effective software, hardware and scanning solutions to the business, utility, and banking marketplace.</p>
    <p>We know that technology is extremely important in giving our customers a competitive advantage. We also realize that the need to keep up with technology is not in the everyday realm of many business owners; expertise is what we offer to provide complete solutions with ongoing support.</p>
    <p>We also believe that the solution should fit your operation instead of disrupting or rebuilding it, and do so simply in a way that lets you wonder why you haven't made the move before now.</p>
    <a class="btn-dark" href="#">Read More &gt;&gt;</a>
  </div>
</section>

<section class="applications">
  <svg style="position:absolute;left:0;top:0" width="1200" height="720" viewBox="0 0 1200 720"><polygon points="0,0 420,0 0,360" fill="#c90c19"/><polygon points="1200,720 740,720 1200,300" fill="#c90c19"/></svg>
  <h2 class="section-title">APPLICATIONS</h2>
  <div class="title-rule"></div>
  <div class="app-grid">
    <div class="app-item" role="img" aria-label="Product photo of a check scanner"></div>
    <div class="app-item featured"><b>+</b>Multi-Function<br>Options<span class="tag"></span></div>
    <div class="app-item" role="img" aria-label="Product photo of a document scanner"></div>
    <div class="app-item" role="img" aria-label="Product photo of a receipt printer"></div>
    <div class="app-item" role="img" aria-label="Product photo of a desktop scanner"></div>
    <div class="app-item" role="img" aria-label="Product photo of a check reader"></div>
    <div class="app-item" role="img" aria-label="Product photo of a payment scanner"></div>
    <div class="app-item" role="img" aria-label="Product photo of a teller scanner"></div>
  </div>
  <span class="view-all">View All &gt;&gt;</span>
</section>

<section class="testimonials">
  <h2 class="section-title"><em>CLIENT</em> TESTIMONIALS</h2>
  <div class="title-rule"></div>
  <div class="review-cards">
    <div class="review-card"><div class="avatar" role="img" aria-label="Client portrait"></div><h4>Daniel Weston</h4><small>Lorem ipsum dolor</small><p>"Lorem ipsum dolor sit amet consec tetuer adipiscing elit. Praesent molestie vitae lacus, tempus non mauris at porta."</p></div>
    <div class="review-card"><div class="avatar" role="img" aria-label="Client portrait"></div><h4>Adam Merton</h4><small>Lorem ipsum dolor</small><p>"Lorem ipsum dolor sit amet consec tetuer adipiscing elit. Praesent molestie vitae lacus, tempus non mauris at porta."</p></div>
    <div class="review-card"><div class="avatar" role="img" aria-label="Client portrait"></div><h4>Carl Brandt</h4><small>Lorem ipsum dolor</small><p>"Lorem ipsum dolor sit amet consec tetuer adipiscing elit. Praesent molestie vitae lacus, tempus non mauris at porta."</p></div>
  </div>
  <span class="slide-arrow prev"><svg width="12" height="12" viewBox="0 0 12 12"><path d="M8 1 3 6l5 5" stroke="#fff" stroke-width="2" fill="none"/></svg></span>
  <span class="slide-arrow next"><svg width="12" height="12" viewBox="0 0 12 12"><path d="m4 1 5 5-5 5" stroke="#fff" stroke-width="2" fill="none"/></svg></span>
</section>

<section class="contact-area">
  <div class="inquiry">
    <h2 class="block-title"><em>QUICK</em> INQUIRY</h2><div class="rule"></div>
    <form class="inquiry-form">
      <div class="field">First Name</div><div class="field">Last Name</div>
      <div class="field full">Email</div>
      <div class="field full">Subject</div>
      <div class="field full message">Message</div>
      <span class="submit">Submit &gt;&gt;</span>
    </form>
  </div>
  <div class="contact-details">
    <h2 class="block-title"><em>CONTACT</em> DETAILS</h2><div class="rule"></div>
    <p>Thanks for visiting our site. We look forward to serving your technology needs, whether large or small.</p>
    <p>Lorem ipsum dolor sit amet, consectetur adipiscing elit, sed do eiusmod tempor incididunt ut labore et dolore magna aliqua.</p>
    <div class="contact-row"><svg width="16" height="16" viewBox="0 0 24 24"><path fill="#e3101f" d="M12 2a7 7 0 0 0-7 7c0 5 7 13 7 13s7-8 7-13a7 7 0 0 0-7-7zm0 9.5A2.5 2.5 0 1 1 12 6.5a2.5 2.5 0 0 1 0 5z"/></svg><div><strong>Address</strong>120 Harbor Lane<br>Springfield, IL 62701</div></div>
    <div class="contact-row"><svg width="16" height="16" viewBox="0 0 24 24"><path fill="#e3101f" d="M6.6 10.8a15 15 0 0 0 6.6 6.6l2.2-2.2c.3-.3.7-.4 1-.2 1.1.4 2.3.6 3.6.6.6 0 1 .4 1 1V20c0 .6-.4 1-1 1A17 17 0 0 1 3 4c0-.6.4-1 1-1h3.5c.6 0 1 .4 1 1 0 1.3.2 2.5.6 3.6.1.3 0 .7-.2 1z"/></svg><div><strong>Call Us</strong>555-014-2270</div></div>
    <div class="contact-row"><svg width="16" height="16" viewBox="0 0 24 24"><path fill="#e3101f" d="M5 3h10v5H5zm-2 6h18v9h-3v3H6v-3H3zm5 7v3h8v-3z"/></svg><div><strong>Fax</strong>555-014-2271</div></div>
    <div class="contact-row"><svg width="16" height="16" viewBox="0 0 24 24"><path fill="#e3101f" d="M2 5h20v14H2zm2 2v.5l8 5 8-5V7z"/></svg><div><strong>Email</strong>freeinfo@r-plumavector.com</div></div>
  </div>
</section>

<section class="map" role="img" aria-label="Street map showing the office location"></section>

<footer class="footer-nav">
  <nav><a href="#">Home</a><a href="#">About Us</a><a href="#">Our Mission</a><a href="#">Applications</a><a href="#">Contact Us</a></nav>
  <div class="social"><span></span><span></span><span></span><span></span></div>
</footer>
<footer class="copyright">Copyright © 2018 r-plumavector Technology. All Rights Reserved.</footer>

</body>
</html>
```